Marta Quinlan Photography needs a unique, creative business card/logo design

I need a design for business cards/logo that is unique and creative in the industry. Simplicity is nice, so not too crowded. Something that will catch my customer's eye and remain in their memory. I am primarily a landscape photographer but will be soon may be branching into boudoir photography as well. I have attached my current card.

Industry/Entity Type

Business

Contact Information for Business Card

Marta Quinlan Photography
Phone: 0439 271 504
Email: MartaQuinlanPhotography@brivomail.net
Website: www.pagerly.net/MartaQuinlanPhotography.Aust

Logo Text

Marta Quinlan Photography

Requirements
Must have
• Contact Details on one side
Should not have
• pixelation

```html
<!DOCTYPE html>
<html lang="en">
<head>
<meta charset="utf-8">
<title>Marta Quinlan Photography – Business Card</title>
<link rel="stylesheet" href="https://fonts.googleapis.com/css2?family=Open+Sans:wght@400;600;700&display=swap">
<style>
  :root {
    --backdrop: #3a322d;
    --card: #0d0d0d;
    --ink: #ffffff;
    --ink-soft: #e6e6e6;
    --mark: #d9d9d9;
  }
  * { margin: 0; padding: 0; box-sizing: border-box; }
  html, body {
    width: 1200px; height: 900px; overflow: hidden;
    background: var(--backdrop);
    font-family: "Open Sans", Arial, sans-serif;
  }
  .canvas {
    position: relative; width: 1200px; height: 900px;
    display: flex; align-items: center; justify-content: center; gap: 60px;
  }
  .card {
    width: 510px; height: 300px;
    background: var(--card);
    position: relative;
    box-shadow: 0 6px 18px rgba(0,0,0,.45);
  }
  .wordmark {
    position: absolute; top: 58px; left: 60px; right: 0;
    text-align: center; color: var(--ink); font-weight: 600;
  }
  .wordmark-name { font-size: 36px; letter-spacing: 1px; line-height: 1; }
  .wordmark-trade { font-size: 14px; letter-spacing: 10px; margin-top: 8px; }
  .contact {
    position: absolute; left: 36px; bottom: 34px; color: var(--ink-soft);
  }
  .contact-name { font-size: 19px; font-weight: 700; color: var(--ink); margin-bottom: 16px; }
  .contact-list { list-style: none; font-size: 13px; line-height: 21px; }
  .contact-list li { display: flex; align-items: center; gap: 10px; }
  .contact-list svg { width: 11px; height: 11px; flex: none; fill: var(--ink-soft); }
  .card-back { display: flex; align-items: center; justify-content: center; }
  .back-mark {
    display: flex; align-items: center; gap: 28px;
    color: var(--mark); font-weight: 600;
  }
  .back-mark .dot {
    width: 170px; height: 170px; border-radius: 50%;
    background: var(--mark); flex: none;
  }
  .back-mark-name {
    font-size: 46px; line-height: 1.1; letter-spacing: 1px;
  }
  .back-mark-name span { display: block; }
</style>
</head>
<body>
<main class="canvas">
  <section class="card card-front">
    <div class="wordmark">
      <div class="wordmark-name">MARTA QUINLAN</div>
      <div class="wordmark-trade">PHOTOGRAPHY</div>
    </div>
    <div class="contact">
      <p class="contact-name">Marta Quinlan</p>
      <ul class="contact-list">
        <li>
          <svg viewBox="0 0 24 24" aria-hidden="true"><path d="M6.6 10.8a15 15 0 0 0 6.6 6.6l2.2-2.2c.3-.3.7-.4 1-.2 1.1.4 2.3.6 3.6.6.6 0 1 .4 1 1V20c0 .6-.4 1-1 1A17 17 0 0 1 3 4c0-.6.4-1 1-1h3.5c.6 0 1 .4 1 1 0 1.3.2 2.5.6 3.6.1.3 0 .7-.2 1z"/></svg>
          0439 271 504
        </li>
        <li>
          <svg viewBox="0 0 24 24" aria-hidden="true"><path d="M2 5h20v14H2z M2 5l10 8 10-8" /></svg>
          MartaQuinlanPhotography@brivomail.net
        </li>
        <li>
          <svg viewBox="0 0 24 24" aria-hidden="true"><rect x="2" y="2" width="20" height="20" rx="3"/></svg>
          /MartaQuinlanPhotography.Aust
        </li>
      </ul>
    </div>
  </section>
  <section class="card card-back">
    <div class="back-mark">
      <span class="dot"></span>
      <p class="back-mark-name"><span>MARTA</span><span>QUINLAN</span></p>
    </div>
  </section>
</main>
</body>
</html>
```